Poster Design Project

Poster with modern feeling to be displayed in office. The text that needs to be included in this poster is below:

Rules
1. If it’s not in writing it doesn’t exist.
2. No such thing as 'off the record.'
3. Do not hold a private conversation in a public place.
4. Don’t believe any number that ends in zero.
5. Never turn down an opportunity to eat or go to the bathroom.
6. Don’t spend any of your own money. Don’t even admit you own a credit card. Don’t spend money that is not yours.
7. Not always a 'right' or 'wrong' answer - 'It depends.'
8. In a campaign, someone has to be in charge – campaigns are a place to foster democracy, not practice it.
9. Assume nothing.
10. If you make a mistake, fix it before analyzing. Bad news doesn’t age well.

Industry/Entity Type

Credit Card

Requirements
Must have
• Rules
7. Not always a “right” or “wrong” answer - 'It depends.' 
9. Assume nothing.

```html
<!DOCTYPE html>
<html lang="en">
<head>
<meta charset="utf-8">
<title>Rules Poster</title>
<link rel="stylesheet" href="https://fonts.googleapis.com/css2?family=Bebas+Neue&family=Oswald:wght@500;600;700&family=Montserrat:ital,wght@0,500;0,700;0,800;1,700;1,800&family=Yellowtail&display=swap">
<style>
  :root{
    --frame:#d9d9d9;
    --gold:#bba66c;
    --gold-light:#cdb983;
    --red:#6b0e16;
    --red-deep:#4d070d;
    --charcoal:#1e1e1e;
    --charcoal-light:#2c2c2c;
    --paper:#e4e4e4;
    --ink:#121212;
    --cream:#d8c68e;
    --white:#ffffff;
  }
  *{margin:0;padding:0;box-sizing:border-box}
  html,body{width:800px;height:1200px;overflow:hidden}
  body{
    background:linear-gradient(135deg,#ececec,var(--frame) 50%,#cfcfcf);
    position:relative;
    font-family:'Oswald',sans-serif;
  }
  .rule{
    position:absolute;left:28px;width:744px;
    display:flex;align-items:center;
    padding-left:107px;padding-right:10px;
    overflow:hidden;
  }
  .text{white-space:nowrap}
  .rule-number{
    position:absolute;left:0;top:2px;width:76px;height:82px;
    display:flex;align-items:center;justify-content:center;
    font-family:'Oswald',sans-serif;font-weight:700;font-size:48px;line-height:1;
  }
  .band-gold{background:linear-gradient(90deg,var(--gold),var(--gold-light) 60%,var(--gold));color:var(--ink)}
  .band-red{background:linear-gradient(180deg,var(--red),var(--red-deep));color:var(--cream)}
  .band-dark{background:linear-gradient(180deg,var(--charcoal-light),var(--charcoal));color:var(--white)}
  .num-red{background:var(--red);color:var(--white)}
  .num-gold{background:var(--gold);color:var(--white)}
  .num-paper{background:var(--paper);color:var(--red)}
  .num-deep{background:var(--red-deep);color:var(--white)}

  .condensed{font-family:'Bebas Neue','Oswald',sans-serif;font-weight:400;text-transform:uppercase;letter-spacing:0;line-height:1}
  .wide{font-family:'Montserrat',sans-serif;font-weight:800;text-transform:uppercase}
  .script{font-family:'Yellowtail','Brush Script MT',cursive;color:var(--white);text-transform:none;font-size:50px;letter-spacing:0;font-weight:400;line-height:1}

  .r1{top:28px;height:107px}
  .r1 .text{font-size:41px}
  .r2{top:140px;height:122px}
  .r2 .text{font-family:'Bebas Neue',sans-serif;font-size:54px;color:var(--gold-light);letter-spacing:-0.5px;line-height:1}
  .r2 .text em{font-style:normal;color:var(--white)}
  .r3{top:268px;height:122px}
  .r3 .text{font-size:22px;line-height:1.5;letter-spacing:5px}
  .r3 em{font-style:italic;color:var(--gold)}
  .r4{top:396px;height:94px}
  .r4 .text{font-size:40px}
  .r4 em{font-style:italic;color:var(--white)}
  .r5{top:498px;height:124px}
  .r5 .text{font-family:'Montserrat',sans-serif;font-weight:700;font-size:25px;line-height:1.6;letter-spacing:1.5px;text-transform:uppercase;color:var(--cream)}
  .r6{top:628px;height:120px}
  .r6 .text{font-family:'Montserrat',sans-serif;font-style:italic;font-weight:700;font-size:19px;line-height:1.3;letter-spacing:3px;text-transform:uppercase}
  .r7{top:754px;height:102px}
  .r7 .text{font-size:34px}
  .r7 em{color:var(--white);font-style:italic}
  .r8{top:862px;height:120px}
  .r8 .text{font-family:'Montserrat',sans-serif;font-weight:700;font-size:24px;line-height:1.3;letter-spacing:1px;text-transform:uppercase;color:var(--cream)}
  .r8 .text b{color:var(--white)}
  .r9{top:988px;height:82px}
  .r9 .rule-number{height:80px;top:0}
  .r9 .text{font-family:'Montserrat',sans-serif;font-style:italic;font-weight:800;font-size:38px;letter-spacing:12px;text-transform:uppercase}
  .r10{top:1076px;height:96px}
  .r10 .rule-number{font-size:46px}
  .r10 .text{font-family:'Montserrat',sans-serif;font-weight:500;font-size:22px;line-height:1.4;letter-spacing:1px;text-transform:uppercase}
  .r10 .text b{font-weight:800}
  .underline{text-decoration:underline;text-decoration-thickness:2px;text-underline-offset:4px}

  .food-icon{display:inline-block;width:40px;height:18px;border-radius:9px;vertical-align:middle;
    background:linear-gradient(180deg,#e9c98d,#b98a4a)}
  .restroom-icon{vertical-align:middle}
</style>
</head>
<body>
  <section class="rule band-gold r1">
    <div class="rule-number num-red">1</div>
    <p class="text condensed">If it’s <span class="underline">not</span> in <span class="script">Writing</span> it doesn’t exist</p>
  </section>

  <section class="rule band-red r2">
    <div class="rule-number num-gold">2</div>
    <p class="text">No such thing as <em>'Off the Record'</em></p>
  </section>

  <section class="rule band-dark r3">
    <div class="rule-number num-paper">3</div>
    <p class="text wide">Do not hold a <em>private</em><br>conversation in a <em>public</em> place</p>
  </section>

  <section class="rule band-gold r4">
    <div class="rule-number num-red">4</div>
    <p class="text condensed">Don't believe any number that ends in <em>zero</em></p>
  </section>

  <section class="rule band-red r5">
    <div class="rule-number num-gold">5</div>
    <p class="text">Never turn down an opportunity to<br>eat <span class="food-icon" role="img" aria-label="Hot dog icon"></span> or go to the bathroom
      <svg class="restroom-icon" width="26" height="26" viewBox="0 0 26 26" aria-label="Restroom icon" role="img">
        <g fill="#f3ead0">
          <circle cx="7" cy="3" r="2.6"/><path d="M4 7h6v9H8.5v9h-3v-9H4z"/>
          <circle cx="19" cy="3" r="2.6"/><path d="M16.5 7h5l2.5 10h-3v8h-4v-8h-3z"/>
        </g>
      </svg>
    </p>
  </section>

  <section class="rule band-dark r6">
    <div class="rule-number num-paper">6</div>
    <p class="text">Don’t spend any of your own money.<br>Don’t even admit you own a credit card.<br>Don’t spend money that is not yours.</p>
  </section>

  <section class="rule band-gold r7">
    <div class="rule-number num-red">7</div>
    <p class="text condensed">Not always a ‘right’ or ‘wrong’ answer - <em>‘It depends.’</em></p>
  </section>

  <section class="rule band-red r8">
    <div class="rule-number num-gold">8</div>
    <p class="text">In a campaign, someone has to be in<br>charge - <b>campaigns are a place to<br>foster democracy, not practice it.</b></p>
  </section>

  <section class="rule band-dark r9">
    <div class="rule-number num-paper">9</div>
    <p class="text">Assume nothing.</p>
  </section>

  <section class="rule band-gold r10">
    <div class="rule-number num-deep">10</div>
    <p class="text">If you make a mistake, fix it <span class="underline">before</span><br>analyzing. <b>Bad news doesn’t age well.</b></p>
  </section>
</body>
</html>
```